Business Folder

I need a fresh, modern design for a business folder. I have our company's colors, logo, and a separate file for just the graphic part of our logo as a design element. No photo, just colors, gradients, and shadows to create depth. I like the idea of a rich grey as the background, however, I realize we'd have to lighten to 'Tax Advisory Services' part of our logo.

The design would just be the 'front' or outside of the folder from Mellowfax. Design file attached. You can find that here under 9 x 12 standard folder, Left and Right Pockets With Slit Both Sides:

https://www.mellowfax-example.com/content.html?id=folderDownloadTemplates&rightMenuId=rightMenu&footerId=bodyFooterStyle6

```html
<!DOCTYPE html>
<html lang="en">
<head>
<meta charset="utf-8">
<title>Lumora Tax Advisory Services – Presentation Folder</title>
<link rel="stylesheet" href="https://fonts.googleapis.com/css2?family=Roboto:wght@300;400;500;700&family=Roboto+Condensed:wght@400;700&display=swap">
<style>
  :root{
    --stage:#1b5a86;
    --navy:#0f4a7c;
    --blue:#1b78b8;
    --sky:#8fd0ea;
    --ice:#e3f3fb;
    --ink:#1b1b1b;
    --grey-text:#555;
    --paper:#ffffff;
    --silver:#e9e9ea;
  }
  *{box-sizing:border-box;margin:0;padding:0}
  html,body{width:1200px;height:1200px;overflow:hidden}
  body{background:var(--stage);font-family:"Roboto",Arial,sans-serif;position:relative}

  .spread{position:absolute;overflow:hidden}
  .outside{left:77px;top:42px;width:749px;height:484px}
  .inside{left:330px;top:595px;width:754px;height:502px}

  .panel{position:absolute;top:0;height:100%}
  .back-cover{left:0;width:375px}
  .front-cover{left:375px;width:374px}

  .pattern-blue{
    position:absolute;inset:0;
    background:
      radial-gradient(ellipse at 20% 20%, rgba(120,200,230,.55), transparent 55%),
      radial-gradient(ellipse at 80% 85%, rgba(110,195,228,.55), transparent 55%),
      linear-gradient(160deg,#cfeaf6 0%,#eef8fc 45%,#bfe3f3 100%);
  }
  .front-cover .pattern-blue{
    background:
      linear-gradient(90deg,rgba(200,200,205,.55) 0%,rgba(255,255,255,0) 18%),
      radial-gradient(ellipse at 85% 15%, rgba(120,200,230,.6), transparent 50%),
      radial-gradient(ellipse at 40% 90%, rgba(110,195,228,.55), transparent 55%),
      linear-gradient(170deg,#d6eef8 0%,#f3fafd 50%,#c3e5f4 100%);
  }
  .pattern-grey{
    position:absolute;inset:0;
    background:
      linear-gradient(90deg,rgba(255,255,255,0) 45%,rgba(200,200,204,.6) 50%,rgba(255,255,255,.9) 52%,rgba(255,255,255,0) 60%),
      radial-gradient(ellipse at 25% 30%, rgba(190,190,195,.7), transparent 55%),
      linear-gradient(160deg,#f1f1f2 0%,#dcdcde 50%,#f4f4f5 100%);
  }

  .company-block{position:absolute;left:22px;top:386px;font-family:"Roboto Condensed",Arial,sans-serif;font-size:8.5px;line-height:11px;color:var(--ink)}
  .company-block strong{font-weight:700}
  .company-block .hours{margin-top:4px;font-weight:700}
  .contact-list{position:absolute;left:218px;top:386px;font-family:"Roboto Condensed",Arial,sans-serif;font-size:8.5px;line-height:11.5px;color:var(--ink)}
  .contact-list dt{float:left;width:31px;clear:left}
  .contact-list dd{margin-left:31px}
  .site-url{position:absolute;font-size:17px;font-weight:300;color:var(--navy);text-align:center;width:100%}
  .back-cover .site-url{top:446px;left:-10px}
  .front-cover .site-url{top:442px}

  .brand{position:absolute;left:44px;top:130px;display:flex;align-items:center;gap:12px}
  .brand-mark{width:26px;height:26px;background:var(--blue)}
  .brand-name{font-size:62px;font-weight:700;color:var(--navy);letter-spacing:1px;line-height:1}
  .headline{position:absolute;top:270px;width:100%;text-align:center;font-size:29px;font-weight:500;line-height:38px;color:var(--navy)}

  .insert-sheet{position:absolute;left:428px;top:30px;width:299px;height:320px;background:var(--paper);box-shadow:0 0 8px rgba(0,0,0,.25)}
  .sheet-brand{display:flex;justify-content:center;align-items:center;gap:6px;margin-top:18px}
  .sheet-brand .brand-mark{width:9px;height:9px}
  .sheet-brand .brand-name{font-size:22px}
  .offer-band{position:absolute;left:0;top:52px;width:100%;height:65px;background:
    linear-gradient(155deg,transparent 62%,#4d93c7 62%),
    linear-gradient(120deg,#1873b3 0%,#1873b3 30%,var(--navy) 30%);color:#fff}
  .offer-text{position:absolute;left:70px;top:11px;width:170px;text-align:center;font-family:"Roboto Condensed",Arial,sans-serif}
  .offer-text .q{font-size:8.5px;font-weight:700;line-height:10px}
  .offer-text .cta{font-size:6.8px;font-weight:700;margin-top:3px}
  .offer-text .fine{font-size:2.6px;line-height:3.4px;margin-top:3px;opacity:.85}
  .offer-icon{position:absolute;left:238px;top:12px}
  .sheet-body{position:absolute;left:18px;top:135px;width:264px;font-size:4.6px;line-height:6.2px;color:var(--grey-text)}
  .sheet-body h2{font-size:10px;font-weight:500;color:var(--navy);line-height:12px;margin-bottom:6px}
  .sheet-body p{margin-bottom:4px}
  .sheet-body h2.second{margin-top:10px}

  .pocket{position:absolute;top:333px;height:169px;overflow:hidden;box-shadow:0 -2px 5px rgba(0,0,0,.18)}
  .pocket-left{left:0;width:373px;border-top-right-radius:16px}
  .pocket-right{left:384px;width:370px;border-top-left-radius:16px}
  .pocket .pattern-blue{background:
    radial-gradient(ellipse at 30% 60%, rgba(110,195,228,.55), transparent 55%),
    radial-gradient(ellipse at 80% 30%, rgba(120,200,230,.45), transparent 50%),
    linear-gradient(160deg,#d9f0f9 0%,#f2fafd 50%,#c3e5f4 100%)}
  .services-title{position:absolute;top:32px;left:0;width:100%;text-align:center;font-size:17px;font-weight:500;color:var(--blue)}
  .service-list{position:absolute;top:62px;left:10px;width:350px;display:flex;justify-content:space-between;list-style:none}
  .service{width:58px;text-align:center;font-size:5.6px;font-weight:500;line-height:7px;color:#333;text-transform:uppercase}
  .service svg{display:block;margin:0 auto 4px;width:24px;height:24px}
</style>
</head>
<body>

<section class="spread outside" aria-label="Folder outside">
  <div class="panel back-cover">
    <div class="pattern-blue" role="img" aria-label="Soft light-blue diamond and dot pattern background"></div>
    <address class="company-block" style="font-style:normal">
      <strong>Lumora Tax Advisory Services, LLC</strong><br>
      1420 Alder Park Drive, Ste. 210<br>
      Cedar Falls, IA 50613
      <div class="hours">Hours: 9:00 am - 5:00 pm (M-F)</div>
    </address>
    <dl class="contact-list">
      <dt>Email</dt><dd>: hello@lumorataxadvisory.example</dd>
      <dt>Local</dt><dd>: 555-014-2290</dd>
      <dt>Toll Free</dt><dd>: 800-555-0147</dd>
      <dt>Fax</dt><dd>: 800-555-0147</dd>
    </dl>
    <p class="site-url">www.lumorataxadvisory.example</p>
  </div>

  <div class="panel front-cover">
    <div class="pattern-blue" role="img" aria-label="Soft light-blue diamond and dot pattern background"></div>
    <div class="brand">
      <span class="brand-mark"></span>
      <span class="brand-name">LUMORA</span>
    </div>
    <h1 class="headline">COMPLETE<br>TAX &amp; WEALTH<br>PLANNING FIRM</h1>
    <p class="site-url">www.lumorataxadvisory.example</p>
  </div>
</section>

<section class="spread inside" aria-label="Folder inside">
  <div class="pattern-grey" role="img" aria-label="Soft grey diamond and dot pattern background"></div>

  <article class="insert-sheet">
    <div class="sheet-brand">
      <span class="brand-mark"></span>
      <span class="brand-name">LUMORA</span>
    </div>
    <div class="offer-band">
      <div class="offer-text">
        <p class="q">Wondering How You Could<br>Create More Tax Efficiency?</p>
        <p class="cta">Request a Tax-Smart Second Opinion!</p>
        <p class="fine">Our tax team will review your past returns<br>and project ways to lower future taxes.</p>
      </div>
      <svg class="offer-icon" width="46" height="44" viewBox="0 0 46 44" aria-hidden="true">
        <g fill="none" stroke="#fff" stroke-width="2.2">
          <path d="M4 14 L23 3 L42 14 Z"/>
          <line x1="4" y1="17" x2="42" y2="17"/>
          <line x1="11" y1="20" x2="11" y2="35"/><line x1="19" y1="20" x2="19" y2="35"/>
          <line x1="27" y1="20" x2="27" y2="35"/><line x1="35" y1="20" x2="35" y2="35"/>
          <line x1="3" y1="38" x2="43" y2="38"/><line x1="1" y1="41.5" x2="45" y2="41.5"/>
        </g>
      </svg>
    </div>
    <div class="sheet-body">
      <h2>Complete Tax &amp; Wealth Planning Firm</h2>
      <p>Planning for retirement is a long journey that calls for flexible solutions. We offer tax-aware investment management and wealth planning for people in or near retirement, built around your goals and reviewed for tax impact.</p>
      <p>Our skilled team works to protect your assets and your legacy with a clear, step-by-step plan for your financial future.</p>
      <p>With our complete approach to tax and retirement planning, you're in expert hands with Lumora.</p>
      <h2 class="second">Complete Tax &amp; Wealth Planning Firm</h2>
      <p>Planning for retirement is a long journey that calls for flexible solutions and careful tax review.</p>
    </div>
  </article>

  <div class="pocket pocket-left">
    <div class="pattern-blue" role="img" aria-label="Soft light-blue diamond and dot pattern background"></div>
  </div>

  <div class="pocket pocket-right">
    <div class="pattern-blue" role="img" aria-label="Soft light-blue diamond and dot pattern background"></div>
    <h2 class="services-title">How We Serve You</h2>
    <ul class="service-list">
      <li class="service">
        <svg viewBox="0 0 24 24" aria-hidden="true"><g fill="none" stroke="#1b78b8" stroke-width="1.8"><path d="M2 8 L12 2 L22 8 Z"/><line x1="5" y1="10" x2="5" y2="19"/><line x1="10" y1="10" x2="10" y2="19"/><line x1="14" y1="10" x2="14" y2="19"/><line x1="19" y1="10" x2="19" y2="19"/><line x1="2" y1="21.5" x2="22" y2="21.5"/></g></svg>
        Tax<br>Planning/Prep
      </li>
      <li class="service">
        <svg viewBox="0 0 24 24" aria-hidden="true"><g fill="none" stroke="#1b78b8" stroke-width="1.8"><rect x="2" y="3" width="20" height="14"/><polyline points="5,14 9,9 13,12 19,6"/><line x1="12" y1="17" x2="8" y2="23"/><line x1="12" y1="17" x2="16" y2="23"/></g></svg>
        Wealth<br>Management
      </li>
      <li class="service">
        <svg viewBox="0 0 24 24" aria-hidden="true"><g fill="none" stroke="#1b78b8" stroke-width="1.8"><rect x="1.5" y="4" width="21" height="16" rx="1"/><rect x="4.5" y="8" width="15" height="8"/><line x1="7" y1="12" x2="17" y2="12"/></g></svg>
        Social Security<br>Planning
      </li>
      <li class="service">
        <svg viewBox="0 0 24 24" aria-hidden="true"><g fill="none" stroke="#1b78b8" stroke-width="1.8"><circle cx="11" cy="13" r="9"/><circle cx="11" cy="13" r="5"/><circle cx="11" cy="13" r="1.5" fill="#1b78b8"/><line x1="11" y1="13" x2="21" y2="3"/><polyline points="17,3 21,3 21,7"/></g></svg>
        Financial<br>Forecasting
      </li>
      <li class="service">
        <svg viewBox="0 0 24 24" aria-hidden="true"><circle cx="12" cy="13" r="9" fill="none" stroke="#1b78b8" stroke-width="1.8"/><path d="M12 13 L12 4 A9 9 0 0 1 20.5 10 Z" fill="#1b78b8"/></svg>
        Risk<br>Management
      </li>
      <li class="service">
        <svg viewBox="0 0 24 24" aria-hidden="true"><g fill="none" stroke="#1b78b8" stroke-width="1.8"><line x1="12" y1="3" x2="12" y2="21"/><line x1="4" y1="6" x2="20" y2="6"/><line x1="7" y1="21.5" x2="17" y2="21.5"/><path d="M1.5 14 L4 7 L6.5 14 Z"/><path d="M17.5 14 L20 7 L22.5 14 Z"/></g></svg>
        Estate<br>Conservation
      </li>
    </ul>
  </div>
</section>

</body>
</html>
```